Painting Company Business Card

Brightwell Painting needs a new business card. See attachments for our logo and current card as an example.
We want to utilize the same colors in the logo, and keep all the information that is currently on it. Just need an updated and modern design.
We are open to loosing the Association Logos if it means a better design.
We are also entertaining a spot for a picture of a headshot of the person listed on the card. Head shot can be finished later.

```html
<!DOCTYPE html>
<html lang="en">
<head>
<meta charset="utf-8">
<title>Brightwell Painting – Business Card</title>
<link rel="stylesheet" href="https://fonts.googleapis.com/css2?family=Comfortaa:wght@400;700&display=swap">
<style>
  :root {
    --brand-green: #6fd000;
    --ink: #2a3236;
    --paper: #ffffff;
  }
  * { margin: 0; padding: 0; box-sizing: border-box; }
  html, body {
    width: 1200px;
    height: 686px;
    overflow: hidden;
    background: var(--paper);
  }
  .card {
    position: relative;
    width: 1200px;
    height: 686px;
    background: var(--paper);
    font-family: "Comfortaa", sans-serif;
    color: var(--ink);
  }
  .accent-tab {
    position: absolute;
    left: 0;
    width: 1200px;
    height: 22px;
  }
  .accent-tab--top { top: 0; }
  .accent-tab--bottom { bottom: 0; }
  .accent-tab polygon { fill: var(--brand-green); }

  .identity {
    position: absolute;
    top: 118px;
    left: 0;
    width: 1200px;
    text-align: center;
  }
  .identity__name {
    font-weight: 700;
    font-size: 118px;
    line-height: 1;
    letter-spacing: 1px;
  }
  .identity__role {
    margin-top: 22px;
    font-weight: 700;
    font-size: 52px;
    line-height: 1;
  }

  .divider {
    position: absolute;
    top: 335px;
    left: 0;
    width: 1200px;
    height: 15px;
    background: var(--brand-green);
  }

  .contact-rule {
    position: absolute;
    left: 366px;
    top: 386px;
    width: 5px;
    height: 240px;
    background: var(--ink);
  }
  .contact-list {
    list-style: none;
    position: absolute;
    left: 240px;
    top: 386px;
  }
  .contact-item {
    display: flex;
    align-items: center;
    height: 86px;
  }
  .contact-item:first-child { height: 70px; }
  .contact-icon {
    width: 92px;
    height: 74px;
    flex: none;
  }
  .contact-text {
    margin-left: 82px;
    font-size: 38px;
    font-weight: 400;
    letter-spacing: 0.5px;
    color: #111;
  }
</style>
</head>
<body>
<div class="card">
  <svg class="accent-tab accent-tab--top" viewBox="0 0 1200 22" aria-hidden="true">
    <polygon points="309,0 891,0 857,22 343,22"/>
  </svg>

  <header class="identity">
    <h1 class="identity__name">Daniel Harper</h1>
    <p class="identity__role">Quality Manager</p>
  </header>

  <div class="divider"></div>
  <div class="contact-rule"></div>

  <ul class="contact-list">
    <li class="contact-item">
      <svg class="contact-icon" viewBox="0 0 92 74" aria-hidden="true">
        <rect x="2" y="6" width="84" height="40" rx="9" fill="none" stroke="#6fd000" stroke-width="4"/>
        <text x="44" y="33" text-anchor="middle" font-family="Arial, sans-serif" font-weight="700" font-size="18" fill="#6fd000">www</text>
        <path d="M52 38 L52 68 L59 61 L65 72 L71 69 L65 58 L74 57 Z" fill="#fff" stroke="#6fd000" stroke-width="3.5" stroke-linejoin="round"/>
      </svg>
      <span class="contact-text">www.brightwellpainting.com</span>
    </li>
    <li class="contact-item">
      <svg class="contact-icon" viewBox="0 0 92 74" aria-hidden="true">
        <path d="M14 30 L46 6 L78 30 L78 70 L14 70 Z" fill="#6fd000"/>
        <rect x="24" y="12" width="44" height="36" fill="#fff" stroke="#6fd000" stroke-width="3"/>
        <text x="46" y="38" text-anchor="middle" font-family="Arial, sans-serif" font-weight="700" font-size="22" fill="#6fd000">@</text>
        <path d="M14 34 L46 56 L78 34 L78 70 L14 70 Z" fill="#6fd000" stroke="#fff" stroke-width="3" stroke-linejoin="round"/>
        <path d="M14 70 L40 50 M78 70 L52 50" stroke="#fff" stroke-width="3"/>
      </svg>
      <span class="contact-text">daniel@brightwellpainting.com</span>
    </li>
    <li class="contact-item">
      <svg class="contact-icon" viewBox="0 0 92 74" aria-hidden="true">
        <circle cx="50" cy="37" r="32" fill="none" stroke="#6fd000" stroke-width="5"/>
        <path d="M37 21 l8 -3 l6 12 l-6 4 q3 9 11 14 l5 -5 l11 7 l-3 8 q-6 5 -15 0 q-14 -8 -20 -24 q-3 -9 3 -13 Z" fill="#6fd000"/>
      </svg>
      <span class="contact-text">262-555-0147</span>
    </li>
  </ul>

  <svg class="accent-tab accent-tab--bottom" viewBox="0 0 1200 22" aria-hidden="true">
    <polygon points="343,0 857,0 891,22 309,22"/>
  </svg>
</div>
</body>
</html>
```